letterhead design using our existing logo

We are a small boutique property management business based in Sydney's Northern Beaches.
We are after a sleek, simple modern letterhead (A4) incorporating our logo and its colours.
Also matching envelope (DL)
I have attached the logo with black text and white text for design options.

Target Market(s)

29-69yo Male and Female

Industry/Entity Type

Property Management

Requirements
Must have
• - Estate Haven logo
• - Address, number and website:
• Suite 7, 18-19 Harlow Parade, Brenton NSW 2187
• Tel: Carl Doyle 0419 267 530 Miriam Kovacs 0407 516 948 www.estatehavenrealty.com.au
Nice to have
• sleek design that looks modern and professional
Should not have
• too many colours or too busy

```html
<!DOCTYPE html>
<html lang="en">
<head>
<meta charset="utf-8">
<title>Estate Haven – Letterhead and DL Envelope</title>
<link rel="stylesheet" href="https://fonts.googleapis.com/css2?family=Source+Sans+3:wght@400;600&display=swap">
<style>
  :root {
    --teal: #2c9ba6;
    --teal-deep: #1a7b8b;
    --ink: #1a1a1a;
    --black-band: #0c0c0e;
    --paper: #fbfbf9;
    --backdrop: #e4e5e6;
  }
  * { margin: 0; padding: 0; box-sizing: border-box; }
  html, body { width: 1200px; height: 1055px; overflow: hidden; }
  body {
    background: var(--backdrop);
    font-family: "Source Sans 3", "Myriad Pro", Arial, sans-serif;
    color: var(--ink);
    position: relative;
  }
  .sheet {
    position: absolute;
    background: var(--paper);
    box-shadow: 0 2px 8px rgba(0,0,0,.18);
    overflow: hidden;
  }
  .letterhead { left: 18px; top: 150px; width: 539px; height: 758px; }
  .envelope-front { left: 568px; top: 239px; width: 619px; height: 261px; background: #fff; }
  .envelope-back { left: 568px; top: 573px; width: 619px; height: 261px; background: #fff; }

  .brand {
    position: absolute;
    display: flex;
    align-items: center;
    gap: 7px;
    font-weight: 600;
    font-size: 23px;
    letter-spacing: .2px;
    color: var(--ink);
    line-height: 1;
  }
  .brand-mark { width: 11px; height: 11px; background: var(--teal); }
  .letterhead .brand { left: 44px; top: 56px; }
  .envelope-front .brand { left: 22px; top: 32px; font-size: 22px; }

  .contact {
    position: absolute;
    left: 357px; top: 44px;
    font-size: 8.4px;
    line-height: 10.8px;
    color: var(--ink);
  }
  .contact-row { display: flex; align-items: center; gap: 4px; }
  .contact-name { color: var(--teal-deep); }
  .contact-icon { width: 7px; height: 7px; flex: none; }
  .abn { margin: 2px 0 0 11px; font-size: 10px; line-height: 12px; }
  .abn-label { color: var(--teal-deep); }

  .letter {
    position: absolute;
    left: 39px; top: 197px;
    width: 459px;
    font-size: 10px;
    line-height: 16.2px;
  }
  .salutation { margin-bottom: 16px; }
  .letter p.body { text-align: justify; margin-bottom: 16px; }
  .signature {
    position: absolute;
    left: 42px; top: 537px;
    width: 166px; height: 48px;
    background: linear-gradient(90deg, rgba(30,30,30,.08), rgba(30,30,30,.02));
    border-radius: 4px;
  }
  .signatory { position: absolute; left: 43px; top: 591px; font-size: 11px; }

  .address { position: absolute; font-size: 8.6px; }
  .letterhead .address { left: 43px; top: 723px; }
  .envelope-front .address { left: 23px; top: 228px; font-size: 8.3px; }

  .band { position: absolute; left: 0; bottom: 0; display: block; }
</style>
</head>
<body>

<section class="sheet letterhead" aria-label="A4 letterhead">
  <div class="brand"><span class="brand-mark"></span>ESTATE HAVEN</div>

  <div class="contact">
    <div class="contact-row">
      <svg class="contact-icon" viewBox="0 0 10 10"><rect width="10" height="10" rx="2" fill="var(--teal-deep)"/><path d="M3 2.5q-1 1 .5 3.5t3.5 1.5l-1-1.2-1 .4q-1-.7-1.5-1.8l.5-.9z" fill="#fff"/></svg>
      <span><span class="contact-name">Carl Doyle</span> 0419 267 530</span>
    </div>
    <div class="contact-row">
      <svg class="contact-icon" viewBox="0 0 10 10"><rect width="10" height="10" rx="2" fill="var(--teal-deep)"/><path d="M3 2.5q-1 1 .5 3.5t3.5 1.5l-1-1.2-1 .4q-1-.7-1.5-1.8l.5-.9z" fill="#fff"/></svg>
      <span><span class="contact-name">Miriam Kovacs</span> 0407 516 948</span>
    </div>
    <div class="contact-row">
      <svg class="contact-icon" viewBox="0 0 10 10"><circle cx="5" cy="5" r="4.3" fill="none" stroke="#777" stroke-width=".9"/><ellipse cx="5" cy="5" rx="1.8" ry="4.3" fill="none" stroke="#777" stroke-width=".7"/><path d="M.7 5h8.6" stroke="#777" stroke-width=".7"/></svg>
      <span>www.estatehavenrealty.com.au</span>
    </div>
    <div class="abn"><span class="abn-label">ABN:</span> 62 517 903 218</div>
  </div>

  <div class="letter">
    <p class="salutation">Dear Client</p>
    <p class="body">Lorem ipsum dolor sit amet, consectetur adipiscing elit. Pellentesque semper purus ornare dolor eleifend aliquam. Integer molestie gravida sem a porttitor. Quisque pulvinar tellus ut ipsum molestie ultricies id non turpis. Phasellus feugiat ornare feugiat. Integer nec velit eu justo laoreet condimentum. Aenean non commodo quam. Phasellus lacinia aliquet turpis. Praesent non elit nec ante porta cursus. Morbi et augue enim, nec ultrices augue. Etiam tempus arcu laoreet metus tristique ultrices.</p>
    <p class="body">Curabitur nec venenatis risus. Integer nec nisi sit amet leo mattis aliquam. Vivamus vulputate tellus quis purus lobortis rutrum. Aenean nec ipsum ut mauris faucibus facilisis vel porttitor neque. Morbi molestie magna id neque scelerisque ut iaculis justo porttitor. Sed est ligula, semper at cursus ac, porttitor ac ipsum. Maecenas pulvinar euismod tempor. Pellentesque habitant morbi tristique senectus et netus et malesuada fames ac turpis egestas. Integer nec velit turpis. Aliquam adipiscing massa sed ipsum commodo id ullamcorper leo volutpat. Sed vitae tellus dui.</p>
    <p class="body">Maecenas vel neque ante, id faucibus ipsum. Suspendisse non neque quis nunc rhoncus bibendum. Fusce sit amet quam quis libero facilisis ultrices. Donec dignissim lorem vel sem sodales mollis. Duis nec sem lorem, at tristique nibh. In rutrum fermentum lectus, nec dictum leo tincidunt in. Nam metus odio, molestie a tempor a, laoreet placerat dui. Fusce sit amet nisi at elit bibendum imperdiet. Sed fringilla nisi non nunc facilisis in ullamcorper justo suscipit. Fusce fermentum tincidunt sagittis.</p>
  </div>

  <div class="signature" role="img" aria-label="Handwritten signature of the managing director"></div>
  <p class="signatory">Managing Director</p>

  <p class="address">Suite 7, 18-19 Harlow Parade,&nbsp; Brenton NSW 2187</p>
  <svg class="band" width="539" height="25" viewBox="0 0 539 25" aria-hidden="true">
    <polygon points="0,7 244,7 232,25 0,25" fill="var(--black-band)"/>
    <polygon points="252,0 539,0 539,25 235,25" fill="var(--teal)"/>
  </svg>
</section>

<section class="sheet envelope-front" aria-label="DL envelope front">
  <div class="brand"><span class="brand-mark"></span>ESTATE HAVEN</div>
  <p class="address">Suite 7, 18-19 Harlow Parade, Brenton NSW 2187</p>
  <svg class="band" width="619" height="26" viewBox="0 0 619 26" aria-hidden="true">
    <polygon points="0,10 277,10 265,26 0,26" fill="var(--black-band)"/>
    <polygon points="286,0 619,0 619,26 268,26" fill="var(--teal)"/>
  </svg>
</section>

<section class="sheet envelope-back" aria-label="DL envelope back">
  <svg width="619" height="90" viewBox="0 0 619 90" aria-hidden="true" style="display:block">
    <path d="M0,0 H619 L606,58 Q600,84 574,84 H45 Q19,84 13,58 Z" fill="var(--teal-deep)"/>
  </svg>
</section>

</body>
</html>
```